Brand new letterhead, business card, email signature etc.

We are a financial company in London, UK. Our website is www.quorvane.com. We're wanting a complete remodel of the company colours, letter head, business cards, email signatures, etc. Looking to keep the same font for the company name. I have upload a colour palette that we want to work with. We're looking for company letterhead for outgoing letters/ correspondence, letterhead for internal documentation, email signatures, e-letters. etc. Ultimately we will redesign the entire website also. It is important that our clients get a strong, secure, warm, trustworthy, solid feeling and first impression.
Updates

Designs look the same

Target Market(s)

Institutional investors, (ultra) high net worth individuals

Industry/Entity Type

Finance, Invesments banking.

Font styles to use
Other font styles liked:
• Current font is "Champagne & Limousines"

Requirements
Must have
• Must use the colours provided on the PDF uploaded to the portal. The purple = main colour. The red = accent colour.
Nice to have
• Nice to use same font as now for the company name "Marlowin". Font is "Champagne & Limousines". Nice to have some reference to the old logo flower, but only subtle.
Should not have
• Do not use the colour red from our website. Use the colours provided on the colour palette PDF that I uploaded in the portal.

```html
<!DOCTYPE html>
<html lang="en">
<head>
<meta charset="utf-8">
<title>Marlowin Business Card</title>
<link rel="stylesheet" href="https://fonts.googleapis.com/css2?family=Josefin+Sans:wght@300&family=Roboto:wght@300;400;700&display=swap">
<style>
  :root {
    --stage: #18161c;
    --main: #33264a;
    --main-deep: #2b1f40;
    --main-soft: #3f3159;
    --accent: #c8102e;
    --ink: #f4f2f7;
    --ink-soft: #d6d0e0;
    --rule: #8d82a3;
  }
  * { margin: 0; padding: 0; box-sizing: border-box; }
  html, body { width: 1200px; height: 963px; overflow: hidden; background: var(--stage); }
  .canvas {
    width: 1200px; height: 963px;
    display: flex; flex-direction: column; align-items: center; justify-content: center; gap: 44px;
  }
  .card {
    position: relative; width: 660px; height: 378px; overflow: hidden;
    background: var(--main);
    box-shadow: 0 12px 30px rgba(0,0,0,.55);
    font-family: "Roboto", sans-serif; color: var(--ink);
  }

  /* front */
  .front-flower {
    position: absolute; left: 430px; top: 190px; width: 230px; height: 188px;
    background: radial-gradient(ellipse at 40% 70%, rgba(200,16,46,.10) 0%, rgba(63,49,89,.55) 45%, rgba(51,38,74,0) 80%);
  }
  .brand { position: absolute; left: 150px; top: 44px; display: flex; align-items: center; gap: 20px; }
  .brand-square { width: 62px; height: 62px; border: 1.5px solid var(--ink); }
  .brand-name {
    font-family: "Josefin Sans", sans-serif; font-weight: 300;
    font-size: 44px; letter-spacing: 12px; color: var(--ink); padding-top: 8px;
  }
  .holder { position: absolute; right: 42px; top: 126px; text-align: right; }
  .holder-name { color: var(--accent); font-size: 22px; font-weight: 400; letter-spacing: 1.5px; }
  .holder-role { font-size: 15px; font-weight: 300; margin-top: 4px; color: var(--ink); }
  .holder-bar { position: absolute; right: 0; top: 128px; width: 18px; height: 50px; background: var(--accent); }
  .offices { position: absolute; left: 150px; top: 156px; font-size: 13px; line-height: 1.5; }
  .office-name { font-weight: 700; }
  .office-address { font-weight: 300; color: var(--ink-soft); }
  .contact-rule { position: absolute; left: 130px; top: 254px; width: 300px; height: 1px; background: var(--rule); }
  .contacts { position: absolute; left: 112px; top: 264px; font-size: 14px; font-weight: 300; }
  .contact { display: flex; align-items: center; gap: 9px; height: 22px; }
  .contact svg { width: 13px; height: 13px; flex: none; }
  .web { position: absolute; left: 302px; top: 286px; font-size: 14px; font-weight: 300; }
  .ribbon { position: absolute; left: 0; top: 0; width: 660px; height: 378px; pointer-events: none; }

  /* back */
  .card-back { background: var(--main-deep); }
  .flower-field {
    position: absolute; left: 0; top: 0; width: 420px; height: 378px;
    background: radial-gradient(ellipse at 60% 55%, var(--main-soft) 0%, #35284c 60%, #2f2344 100%);
    clip-path: polygon(0 0, 100% 0, 62% 100%, 0 100%);
  }
  .back-name {
    position: absolute; right: 54px; bottom: 46px;
    font-family: "Josefin Sans", sans-serif; font-weight: 300;
    font-size: 38px; letter-spacing: 11px; color: var(--ink);
  }
</style>
</head>
<body>
<main class="canvas">
  <section class="card card-front" aria-label="Business card front">
    <div class="front-flower" role="img" aria-label="Faint flower illustration in soft purple tones"></div>

    <div class="brand">
      <span class="brand-square"></span>
      <span class="brand-name">MARLOWIN</span>
    </div>

    <div class="holder">
      <p class="holder-name">EDWIN CARROW</p>
      <p class="holder-role">Manager</p>
    </div>
    <span class="holder-bar"></span>

    <div class="offices">
      <p class="office-name">Marlowin (IOM) Limited</p>
      <p class="office-address">Tallow House, Douglas, Isle of Man, IM98 2QL</p>
      <p class="office-name">Marlowin Group Limited</p>
      <p class="office-address">9th Floor, 14 Aldgate Row, London, EC3N 7PB</p>
    </div>
    <span class="contact-rule"></span>

    <div class="contacts">
      <p class="contact">
        <svg viewBox="0 0 16 16" aria-hidden="true"><path d="M4 1.5l2.5 3-1.6 1.6c.8 1.8 2.2 3.2 4 4l1.6-1.6 3 2.5-1.5 2.5C6.5 13.5 2.5 9.5 1.5 3z" fill="none" stroke="#c8102e" stroke-width="1.4" stroke-linejoin="round"/></svg>
        123-555-0147
      </p>
      <p class="contact">
        <svg viewBox="0 0 16 16" aria-hidden="true"><rect x="1.5" y="3.5" width="13" height="9" fill="none" stroke="#c8102e" stroke-width="1.4"/><path d="M1.5 3.5L8 9l6.5-5.5" fill="none" stroke="#c8102e" stroke-width="1.4"/></svg>
        info@quorvane.com
      </p>
    </div>
    <p class="contact web">
      <svg viewBox="0 0 16 16" aria-hidden="true"><circle cx="8" cy="8" r="6.5" fill="none" stroke="#c8102e" stroke-width="1.3"/><ellipse cx="8" cy="8" rx="3" ry="6.5" fill="none" stroke="#c8102e" stroke-width="1.1"/><path d="M1.5 8h13M2.5 5h11M2.5 11h11" stroke="#c8102e" stroke-width="1.1"/></svg>
      www.quorvane.com
    </p>

    <svg class="ribbon" viewBox="0 0 660 378" aria-hidden="true">
      <polygon points="0,318 0,334 262,378 300,378" fill="var(--accent)"/>
      <polygon points="292,370 470,370 478,378 300,378" fill="var(--ink)"/>
    </svg>
  </section>

  <section class="card card-back" aria-label="Business card back">
    <div class="flower-field" role="img" aria-label="Subtle embossed flower illustration in deep purple tones"></div>
    <p class="back-name">MARLOWIN</p>
  </section>
</main>
</body>
</html>
```